Design some Business Cards

Thank you so much for viewing my contest ! Please be creative
I need some business cards with a cool design, simple and professional.
Below i will add 2 Logos. I want a matte black Background Entry, and a white background entry both front and back. PLEASE KEEP ORIGINAL LOGO COLORS
Please add to the back of the card
Service/Repair/Installations
Duct cleaning services
Miami Dade/Broward County
Call now for a free quote
Special Duct Cleaning Prices
I will need to include contact info for example:
@clearbreezeair
Email
Phone Number
Thank you any questions feel free to contact me.!
I appreciate any creative work!

```html
<!DOCTYPE html>
<html lang="en">
<head>
<meta charset="utf-8">
<title>Clear Breeze Business Cards</title>
<link rel="stylesheet" href="https://fonts.googleapis.com/css2?family=Lato:wght@400;700;900&display=swap">
<style>
  :root {
    --page: #2a2d31;
    --card: #0f0f10;
    --blue: #2f7fb3;
    --blue-deep: #1f5f8c;
    --red: #e8222b;
    --text-soft: #4b93c4;
    --text-muted: #3d7eab;
  }
  * { margin: 0; padding: 0; box-sizing: border-box; }
  html, body { width: 1200px; height: 900px; overflow: hidden; }
  body {
    background: var(--page);
    font-family: "Lato", sans-serif;
    position: relative;
  }
  .card {
    position: absolute;
    width: 620px;
    height: 354px;
    border-radius: 22px;
    background: var(--card);
    overflow: hidden;
    box-shadow: 0 18px 40px rgba(0,0,0,0.35);
  }
  .card__shapes { position: absolute; inset: 0; width: 100%; height: 100%; }
  .card--back { left: 500px; top: 90px; }
  .card--front { left: 80px; top: 460px; }

  /* front */
  .brand-front {
    position: absolute; left: 0; right: 0; top: 58px;
    display: flex; flex-direction: column; align-items: center;
  }
  .brand-front__mark {
    width: 70px; height: 70px; border-radius: 50%;
    border: 4px solid var(--blue);
    margin-bottom: 14px;
  }
  .brand-front__name {
    font-weight: 900; font-size: 46px; letter-spacing: 1px;
    color: var(--blue); line-height: 1;
  }
  .brand-front__tagline {
    margin-top: 6px;
    font-weight: 700; font-size: 13px; letter-spacing: 7px;
    color: var(--red);
  }
  .follow {
    position: absolute; left: 40px; bottom: 16px;
    display: flex; align-items: center; gap: 8px;
    color: #fff; font-size: 15px;
  }
  .follow__dot { width: 18px; height: 18px; border-radius: 50%; background: #fff; }

  /* back */
  .brand-back {
    position: absolute; right: 44px; top: 26px;
    display: flex; flex-direction: column; align-items: center; gap: 6px;
  }
  .brand-back__mark { width: 34px; height: 34px; border-radius: 50%; border: 3px solid var(--blue); }
  .brand-back__name { font-weight: 900; font-size: 14px; color: var(--blue); letter-spacing: .5px; }
  .person { position: absolute; left: 92px; top: 70px; }
  .person__name { color: var(--text-soft); font-size: 26px; font-weight: 400; letter-spacing: .5px; }
  .person__role { color: var(--text-muted); font-size: 13px; }
  .contacts {
    position: absolute; left: 92px; top: 138px; width: 470px;
    display: grid; grid-template-columns: 170px 1fr; gap: 8px 18px;
    color: var(--text-muted); font-size: 12px;
  }
  .contact { display: flex; align-items: flex-start; gap: 7px; line-height: 1.3; }
  .contact svg { flex: none; width: 13px; height: 13px; margin-top: 1px; }
  .services {
    position: absolute; left: 92px; top: 206px;
    color: var(--text-soft); font-size: 18px; line-height: 1.2;
  }
  .services__rule {
    position: absolute; left: 92px; top: 262px; width: 470px; height: 2px;
    background: var(--blue);
  }
</style>
</head>
<body>

<section class="card card--back">
  <svg class="card__shapes" viewBox="0 0 620 354" aria-hidden="true">
    <rect x="0" y="0" width="58" height="354" fill="var(--blue)"/>
    <path d="M58 0 L58 40 C66 46 70 52 70 60 L70 354 L58 354 Z" fill="var(--card)"/>
    <path d="M300 354 C430 330 540 300 620 230 L620 354 Z" fill="var(--blue)"/>
    <path d="M250 346 C400 336 530 300 620 222" fill="none" stroke="var(--red)" stroke-width="7"/>
  </svg>
  <div class="brand-back">
    <div class="brand-back__mark"></div>
    <div class="brand-back__name">CLEAR BREEZE</div>
  </div>
  <div class="person">
    <div class="person__name">DARA KELLAN</div>
    <div class="person__role">Managing Director</div>
  </div>
  <div class="contacts">
    <div class="contact">
      <svg viewBox="0 0 16 16"><path d="M4 1 L6.5 4.5 L5 6 C6 8.5 7.5 10 10 11 L11.5 9.5 L15 12 L13 15 C7 14.5 1.5 9 1 3 Z" fill="var(--text-muted)"/></svg>
      <span>+1 305 555 0147</span>
    </div>
    <div class="contact">
      <svg viewBox="0 0 16 16"><rect x="1" y="3" width="14" height="10" rx="1.5" fill="none" stroke="var(--text-muted)" stroke-width="1.6"/><path d="M1.5 4 L8 9 L14.5 4" fill="none" stroke="var(--text-muted)" stroke-width="1.6"/></svg>
      <span>hello@clearbreeze.co</span>
    </div>
    <div class="contact">
      <svg viewBox="0 0 16 16"><rect x="2" y="2" width="12" height="12" rx="3" fill="var(--text-muted)"/></svg>
      <span>@clearbreezeair</span>
    </div>
    <div class="contact">
      <svg viewBox="0 0 16 16"><path d="M8 15 C4 10 3 8 3 6 A5 5 0 0 1 13 6 C13 8 12 10 8 15 Z" fill="var(--text-muted)"/><circle cx="8" cy="6" r="2" fill="var(--card)"/></svg>
      <span>Suite 23, 12 Palm Road,<br>Miami, FL</span>
    </div>
  </div>
  <div class="services">
    <div>Service/Repair/Installations</div>
    <div>Duct cleaning services</div>
  </div>
  <div class="services__rule"></div>
</section>

<section class="card card--front">
  <svg class="card__shapes" viewBox="0 0 620 354" aria-hidden="true">
    <rect x="0" y="300" width="620" height="54" fill="var(--blue)"/>
    <path d="M300 300 C440 296 550 260 620 196 L620 354 L300 354 Z" fill="var(--blue)"/>
    <path d="M250 300 C420 298 540 262 620 186" fill="none" stroke="var(--red)" stroke-width="8"/>
  </svg>
  <div class="brand-front">
    <div class="brand-front__mark"></div>
    <div class="brand-front__name">CLEAR BREEZE</div>
    <div class="brand-front__tagline">AIR CONDITIONING</div>
  </div>
  <div class="follow">
    <span>Follow Us:</span>
    <span class="follow__dot"></span>
    <span class="follow__dot"></span>
    <span class="follow__dot"></span>
    <span class="follow__dot"></span>
  </div>
</section>

</body>
</html>
```